finlo-welt.de
Zielgruppe
Alle die kein Geld haben :-)
Aufgabenstellung
Unter finlo-welt.de sollen Informationen rund um Kredite, Kreditkarten, Bonvia usw. entstehen. Diese werden dann unter Subdomains wir konto.finlo-welt.de oder kreditkarte.finlo-welt.de laufen. Die Domain finlo-welt.de soll die Hauptdomain werden wofür ein Logo und ein Layout benötigt wird. Auf den einzelnen Seiten sollen später Reporte verkauft werden und relativ viel mit Plunko Werbung gearbeitet werden. Hier ein paar Beipspiele www.zahlwerk-mohnel.biz, www.lumvesta88.de, www.tanne-blau-heft.de, www.nordlicht-mappe-brief.de
Die genannten Seiten sind keine Meisterleistung in Design und sollen nur in etwa Inhalte und die Einbindung von Plunko Adbox wieder geben. Menüpunkte sind immer gleich und werden sein mit den Untertiteln wie bei www.zahlwerk-mohnel.biz.

```html
<!DOCTYPE html>
<html lang="de">
<head>
<meta charset="utf-8">
<title>finlo-welt.de – Startseite</title>
<link href="https://fonts.googleapis.com/css2?family=Open+Sans:wght@400;600;700&display=swap" rel="stylesheet">
<style>
  :root {
    --navy: #2b3a55;
    --navy-dark: #1f2b42;
    --navy-light: #56698a;
    --orange: #f39a1e;
    --orange-deep: #f07c00;
    --text: #3a3f4c;
    --text-soft: #6c7280;
    --muted: #8c93a0;
    --line: #cfd3da;
    --band: #e9eaec;
    --white: #ffffff;
    --tick: #7fba3d;
  }
  * { box-sizing: border-box; margin: 0; padding: 0; }
  html, body { width: 1200px; height: 1070px; overflow: hidden; background: var(--white); }
  body { position: relative; font-family: "Open Sans", Verdana, sans-serif; color: var(--text); }

  .brand { position: absolute; left: 172px; top: 62px; display: flex; align-items: center; gap: 14px; }
  .brand-mark { width: 52px; height: 52px; background: var(--navy); }
  .brand-name { font-size: 26px; font-weight: 700; color: var(--navy); }

  .main-nav {
    position: absolute; left: 90px; top: 170px; width: 1026px; height: 92px;
    background: linear-gradient(#4a5a78 0%, var(--navy) 55%, var(--navy-dark) 100%);
    border-bottom: 4px solid #9aa6ba;
  }
  .nav-item { position: absolute; top: 0; height: 88px; padding-top: 28px; }
  .nav-item.active {
    left: 18px; width: 200px; padding-left: 30px;
    background: linear-gradient(#6c7c98, #4d5d7b);
  }
  .nav-item.active::after {
    content: ""; position: absolute; left: 92px; bottom: 0;
    border: 7px solid transparent; border-bottom-color: var(--orange);
  }
  .nav-title { display: block; font-size: 15px; color: #c4cbd8; }
  .nav-sub { display: block; font-size: 10px; color: #a7b0c0; margin-top: 1px; }
  .active .nav-title { color: var(--white); }
  .active .nav-sub { color: #e6e9ef; font-weight: 600; }

  .intro { position: absolute; left: 90px; top: 278px; width: 508px; font-size: 11.5px; line-height: 20px; }
  .intro h1 { font-size: 16px; font-weight: 600; color: var(--orange); margin-bottom: 18px; }
  .intro p { margin-bottom: 20px; }
  .intro h2 { font-size: 11.5px; font-weight: 700; color: var(--navy-dark); margin: 10px 0 14px; }
  .intro ul { list-style: none; margin: 0 0 46px 40px; color: var(--text-soft); }
  .intro li::before { content: "+ "; color: var(--text); font-weight: 700; }

  .hero-photo {
    position: absolute; left: 608px; top: 274px; width: 508px; height: 276px;
    background: linear-gradient(135deg, #1c3a86 0%, #3b63b4 40%, #c9d0d8 70%, #8d949c 100%);
  }
  .ad-slot {
    position: absolute; border: 1px solid var(--line); background: var(--white);
    display: flex; align-items: center; justify-content: center;
    font-size: 13px; color: var(--muted);
  }
  .ad-top { left: 608px; top: 567px; width: 508px; height: 75px; }
  .ad-bottom { left: 92px; top: 915px; width: 1014px; height: 110px; }

  .feature-band {
    position: absolute; left: 90px; top: 660px; width: 1026px; height: 48px;
    background: linear-gradient(var(--band), var(--white));
    border-top: 2px solid #d6d8dc;
  }
  .btn-tab {
    position: absolute; top: 684px; height: 44px; padding: 0 17px;
    display: flex; align-items: center; font-size: 15px; font-weight: 700; color: var(--navy-dark);
    background: linear-gradient(#ffc043, var(--orange-deep));
    border: 1px solid #e07a00; border-radius: 2px;
  }
  .btn-left { left: 104px; width: 174px; }
  .btn-right { left: 585px; width: 251px; }

  .topic-list { position: absolute; left: 116px; top: 750px; width: 420px; list-style: none; display: grid; grid-template-columns: 268px 150px; row-gap: 13px; }
  .topic-list li { display: flex; align-items: center; gap: 14px; font-size: 12px; font-weight: 700; color: var(--navy-dark); height: 20px; }
  .topic-list li.current { color: var(--orange-deep); }
  .topic-list svg { flex: none; }

  .help-text { position: absolute; left: 588px; top: 744px; width: 512px; font-size: 11px; line-height: 18px; color: var(--text-soft); }
  .help-text p { margin-bottom: 18px; }
  .help-text strong { color: var(--navy-dark); }

  .site-footer { position: absolute; left: 92px; top: 1040px; width: 994px; display: flex; justify-content: space-between; font-size: 10px; color: var(--muted); }
  .footer-links { font-weight: 700; color: #555b66; }
</style>
</head>
<body>
  <header class="brand">
    <span class="brand-mark"></span>
    <span class="brand-name">finlo-welt.de</span>
  </header>

  <nav class="main-nav">
    <div class="nav-item active"><span class="nav-title">Startseite</span><span class="nav-sub">Infos zu unserem Report</span></div>
    <div class="nav-item" style="left:253px"><span class="nav-title">Bestellen</span><span class="nav-sub">Bestellen Sie unseren Report</span></div>
    <div class="nav-item" style="left:442px"><span class="nav-title">Kontakt</span><span class="nav-sub">Treten Sie mit uns in Kontakt</span></div>
    <div class="nav-item" style="left:636px"><span class="nav-title">Datenschutz</span><span class="nav-sub">Hinweise zum Datenschutz</span></div>
    <div class="nav-item" style="left:817px"><span class="nav-title">Impressum</span><span class="nav-sub">Unsere Anschrift für Fragen</span></div>
  </nav>

  <section class="intro">
    <h1>Herzlich Willkommen auf finlo-welt.de</h1>
    <p>Lorem ipsum dolor sit amet, consetetur sadipscing elitr, sed diam nonumy eirmod tempor invidunt ut labore et dolore magna aliquyam erat, sed diam voluptua. At vero eos et accusam et justo duo dolores et ea rebum. Stet clita kasd gubergren, no sea takimata sanctus est Lorem ipsum dolor sit amet. Lorem ipsum dolor sit amet, consetetur sadipscing elitr, sed diam nonumy eirmod tempor invidunt ut labore et dolore magna aliquyam erat, sed diam voluptua. At vero eos et accusam et justo duo dolores et ea rebum. Stet clita kasd guberg</p>
    <h2>ren, no sea takimata sanctus est Lorem ip</h2>
    <ul>
      <li>sum dolor sit amet. Lorem ipsum dolor sit amet, cons</li>
      <li>etetur sadipscing elitr, sed diam nonumy eirmod tempor in</li>
      <li>vidunt ut labore et dolore magna aliquyam erat, sed diam</li>
      <li>voluptua. At vero eos et accusam et justo duo dolores et ea reb</li>
    </ul>
    <p>um. Stet clita kasd gubergren, no sea takimata sanctus est Lorem ipsum dolor sit Duis autem vel eum iriure dolor in hendrerit in vulputate velit esse molestie conse e eu feugiat nulla facilisis at vero eros et accumsan et iusto odio dignissim qui bla tum zzril delenit augue duis dolore te feugait nulla facilisi. Lorem ipsum dolor sit</p>
  </section>

  <div class="hero-photo" role="img" aria-label="Foto: Geschäftsmann im blauen Hemd arbeitet von oben gesehen an Tastatur und Unterlagen"></div>
  <aside class="ad-slot ad-top">Werbe Fläche für Plunko Anzeige</aside>

  <div class="feature-band"></div>
  <div class="btn-tab btn-left">Was tun wir alles?</div>
  <div class="btn-tab btn-right">Wie können wir Ihnen helfen?</div>

  <ul class="topic-list">
    <li class="current"><svg width="14" height="14" viewBox="0 0 14 14"><circle cx="7" cy="7" r="7" fill="var(--tick)"/><path d="M3.8 7.2l2.2 2.2 4.2-4.4" stroke="#fff" stroke-width="1.8" fill="none"/></svg>Was tun, wenn Schulden da sind?</li>
    <li><svg width="14" height="14" viewBox="0 0 14 14"><circle cx="7" cy="7" r="7" fill="var(--tick)"/><path d="M3.8 7.2l2.2 2.2 4.2-4.4" stroke="#fff" stroke-width="1.8" fill="none"/></svg>Geld verdienen!</li>
    <li><svg width="14" height="14" viewBox="0 0 14 14"><circle cx="7" cy="7" r="7" fill="var(--tick)"/><path d="M3.8 7.2l2.2 2.2 4.2-4.4" stroke="#fff" stroke-width="1.8" fill="none"/></svg>Schützen Sie sich vor Abzocke!</li>
    <li><svg width="14" height="14" viewBox="0 0 14 14"><circle cx="7" cy="7" r="7" fill="var(--tick)"/><path d="M3.8 7.2l2.2 2.2 4.2-4.4" stroke="#fff" stroke-width="1.8" fill="none"/></svg>Geld sparen!</li>
    <li><svg width="14" height="14" viewBox="0 0 14 14"><circle cx="7" cy="7" r="7" fill="var(--tick)"/><path d="M3.8 7.2l2.2 2.2 4.2-4.4" stroke="#fff" stroke-width="1.8" fill="none"/></svg>Wenn der Gerichtsvollzieher kommt!</li>
    <li><svg width="14" height="14" viewBox="0 0 14 14"><circle cx="7" cy="7" r="7" fill="var(--tick)"/><path d="M3.8 7.2l2.2 2.2 4.2-4.4" stroke="#fff" stroke-width="1.8" fill="none"/></svg>Wichtige Regeln!</li>
  </ul>

  <section class="help-text">
    <p>Mit unserem eBook "So befreien Sie sich aus der Schuldenfalle"! Das eBook enthält die besten Tipps und Tricks um Schulden loszuwerden. Wir e.</p>
    <p><strong>Schulden</strong> sind, wie diese entstehen und vor allem, wie Sie diese wieder los werden. Außerdem gehen wir auch auf Themen wie die Schuldnerberatung, die eidesstattliche Versicherung (oft auch Offenbarungseid genannt) und die Pfändung ein.</p>
    <p>Sie haben also hiermit ein eBook welches alle Themen die rund um Schulden passieren und verdienen können und Sie erhalten nützliche Formulare direkt zum Aus.</p>
  </section>

  <aside class="ad-slot ad-bottom">Werbe Fläche für Plunko Anzeige</aside>

  <footer class="site-footer">
    <span>Copyright by finlo-welt.de 2010</span>
    <span class="footer-links">AGB - Imprint - FAQ</span>
  </footer>
</body>
</html>
```